Bright Harbor Consulting

I need a business card design and for my consulting business. I provide outsourced CFO services for start-ups and high growth companies. I call my company Bright Harbor Co because building a company is similar to building a stone pathway, selecting each stone and planning several stones head in order to properly place them - all while keeping an eye on the final design and curve of the path. The underlying idea I want to express with my marketing images is that I'm someone that you can count on to help build your business and be there step by step to help. I'm not the old gray-haired CFO that many folks think of. :) I've included a one-page summery that I'm working on, it includes a summary of what I do. I've used a muted pathway and with greens in the header , and do like the green, but am open to other colors if they work well. Would like something that looks like a pathway, but a more abstract version instead of a picture.

```html
<!DOCTYPE html>
<html lang="en">
<head>
<meta charset="utf-8">
<title>Bright Harbor Co – Business Card</title>
<link rel="stylesheet" href="https://fonts.googleapis.com/css2?family=Marcellus&family=Tinos:wght@400;700&display=swap">
<style>
  :root {
    --brand-green: #12915a;
    --soft-green: #c8dccd;
    --ink-gray: #3c4641;
    --muted-gray: #7f8f86;
    --paper-white: #ffffff;
    --backdrop: #e9ebea;
    --card-w: 760px;
    --card-h: 434px;
  }
  * { box-sizing: border-box; margin: 0; padding: 0; }
  html, body {
    width: 1200px;
    height: 1000px;
    overflow: hidden;
    background: var(--backdrop);
  }
  .sheet {
    width: 1200px;
    height: 1000px;
    display: flex;
    flex-direction: column;
    align-items: center;
    justify-content: space-evenly;
  }
  .card {
    position: relative;
    width: var(--card-w);
    height: var(--card-h);
    overflow: hidden;
    box-shadow: 0 6px 18px rgba(0, 0, 0, 0.12);
  }

  /* Front */
  .card--front {
    background: var(--brand-green);
    display: flex;
    flex-direction: column;
    align-items: center;
    justify-content: center;
    color: var(--paper-white);
    font-family: "Marcellus", serif;
  }
  .brand-dot {
    width: 70px;
    height: 70px;
    border-radius: 50%;
    background: var(--paper-white);
    margin-bottom: 26px;
  }
  .brand-name {
    font-size: 40px;
    letter-spacing: 3px;
    line-height: 1;
    white-space: nowrap;
  }
  .brand-tagline {
    font-size: 16px;
    letter-spacing: 3px;
    margin-top: 8px;
    white-space: nowrap;
  }

  /* Back */
  .card--back {
    background: var(--brand-green);
    font-family: "Tinos", serif;
    color: var(--paper-white);
  }
  .path-shape {
    position: absolute;
    inset: 0;
    width: 100%;
    height: 100%;
  }
  .back-brand {
    position: absolute;
    left: 40px;
    top: 170px;
    width: 280px;
    display: flex;
    flex-direction: column;
    align-items: center;
    font-family: "Marcellus", serif;
    color: var(--ink-gray);
  }
  .back-brand .brand-dot {
    width: 52px;
    height: 52px;
    background: var(--brand-green);
    margin-bottom: 16px;
  }
  .back-brand .brand-name {
    font-size: 25px;
    letter-spacing: 1.5px;
  }
  .back-brand .brand-tagline {
    font-size: 11px;
    letter-spacing: 2.5px;
    color: var(--muted-gray);
    margin-top: 6px;
  }
  .person {
    position: absolute;
    left: 470px;
    top: 60px;
  }
  .person-name {
    font-size: 27px;
    font-weight: 700;
  }
  .person-name .credential {
    font-size: 18px;
  }
  .person-role {
    font-size: 17px;
    margin-top: 2px;
  }
  .contact {
    position: absolute;
    left: 430px;
    bottom: 58px;
    list-style: none;
    font-size: 19px;
    line-height: 1.55;
    letter-spacing: 0.5px;
  }
</style>
</head>
<body>
<main class="sheet">
  <section class="card card--front" aria-label="Card front">
    <span class="brand-dot" aria-hidden="true"></span>
    <div class="brand-name">BRIGHT HARBOR CO</div>
    <div class="brand-tagline">CONSULTING SERVICES</div>
  </section>

  <section class="card card--back" aria-label="Card back">
    <svg class="path-shape" viewBox="0 0 760 434" preserveAspectRatio="none" aria-hidden="true">
      <path d="M0 0 H250 C330 20 360 90 350 170 C340 250 330 340 390 434 H0 Z" fill="var(--soft-green)"/>
      <path d="M0 30 C60 45 95 90 82 130 C72 160 40 185 0 195 Z" fill="var(--brand-green)"/>
    </svg>

    <div class="back-brand">
      <span class="brand-dot" aria-hidden="true"></span>
      <div class="brand-name">BRIGHT HARBOR CO</div>
      <div class="brand-tagline">CONSULTING SERVICES</div>
    </div>

    <div class="person">
      <div class="person-name">Dana Whitfield, <span class="credential">CPA</span></div>
      <div class="person-role">Consultant</div>
    </div>

    <ul class="contact">
      <li>p : 555- 014- 2286</li>
      <li>e : dana@brightharborco.com</li>
    </ul>
  </section>
</main>
</body>
</html>
```